Landing Page
Very good design - and the work is quick and responsive.
Zielgruppe
We are an institution for the communication and dissemination of contemporary art and design in Japan and Europe. We primarily organise exhibitions of upcoming Japanese artists at European venues; and also European artists at venues in Japan.
Our target groups are sponsors (companies, foundations) which are willing to sponsor exhibition programs. In addition, we want to appeal to artists who are interested in expanding their regional footprint.
Our purpose is to create a place to meet and interact with people outside of their circles through art appreciation, as well as support challenges of upcoming artists.
We have 3 product lines:
Service 1 – Exhibition organisation
We organise exhibitions of emerging Japanese artists at European venues, and European artists in Japan.
Curatorial, logistics, venue coordination.
Service 2 – Sponsorship Programs
We work with companies and foundations to create meaningful cultural projects.
Tailored sponsoring proposals with visibility and community engagement.
Service 3 – Artist Support
We help artists expand their network and create sustainable international careers.
Aufgabenstellung
We already have company logo. The logo includes two colours (Blue: 142c46 and
pink: eb5c5b).
I want a very simple and modern landing page with 4 sections: 1) About, 2) Services, 3) Latest Insight (blogs), and 4) Contact. I need two tabs with same design; one of which in English and the other one will be translated in Japanese by myself.
PLEASE use WIX, and Adobe Illustrator (if relevant).

```html
<!DOCTYPE html>
<html lang="en">
<head>
<meta charset="utf-8">
<title>Veranto – Connecting Japanese and European Art</title>
<link href="https://fonts.googleapis.com/css2?family=Michroma&family=Poppins:wght@400;500&display=swap" rel="stylesheet">
<style>
:root{
  --navy:#142c46;
  --navy-card:#223a56;
  --coral:#eb5c5b;
  --ink:#142c46;
  --muted:#4a5a6c;
  --soft:#f8f8f8;
  --field:#f3f3f3;
  --white:#ffffff;
  --line:#d9dde2;
}
*{margin:0;padding:0;box-sizing:border-box}
html,body{width:1200px;height:3232px;overflow:hidden}
body{position:relative;background:var(--white);font-family:"Poppins",sans-serif;color:var(--ink)}
.abs{position:absolute}
.display{font-family:"Michroma",sans-serif;color:var(--navy);text-transform:uppercase;letter-spacing:-0.5px;font-weight:400}
.btn{position:absolute;background:var(--coral);color:var(--white);font-size:12px;display:flex;align-items:center;justify-content:center}
.brand{display:flex;align-items:center;gap:12px;font-family:"Poppins",sans-serif;color:var(--navy);letter-spacing:3px;text-transform:uppercase}
.brand-dot{border:2px solid var(--navy);border-radius:50%}
.art{position:absolute}

/* header */
.nav{position:absolute;top:30px;left:335px;display:flex;gap:0;font-size:12px}
.nav a{position:absolute;white-space:nowrap;color:var(--ink);text-decoration:none}

/* hero */
.hero-title{left:123px;top:232px;font-size:38px;line-height:43px}
.hero-sub{left:123px;top:375px;font-size:12px;line-height:18px;width:460px}
.view-box{left:1004px;top:439px;width:122px;height:116px;background:var(--navy);color:var(--white);font-size:12.5px;line-height:16px;padding:18px 0 0 19px}
.corner-arrow{position:absolute;width:20px;height:20px;background:var(--coral);display:flex;align-items:center;justify-content:center}

/* who */
.who-bg{left:0;top:700px;width:1200px;height:1157px;background:var(--soft)}
.who-card{left:127px;top:784px;width:302px;height:352px;background:var(--white);border-bottom:6px solid var(--line)}
.who-title{left:481px;top:796px;font-size:28px}
.who-text{left:481px;top:850px;width:540px;font-size:11px;line-height:18px;color:var(--muted)}
.checks{left:481px;top:978px;list-style:none;font-size:16px;line-height:25px;color:var(--ink)}
.checks li{display:flex;align-items:center;gap:11px}

/* services */
.svc-title{left:0;top:1297px;width:1200px;text-align:center;font-size:29px;line-height:34px}
.svc-card{position:absolute;top:1422px;width:305px;height:341px}
.svc-label{position:absolute;left:14px;top:284px;width:277px;height:43px;background:var(--white);font-size:18px;font-weight:500;display:flex;align-items:center;padding-left:22px}
.svc-label.dark{background:var(--navy);color:var(--white)}

/* insights */
.ins-bg{left:0;top:1857px;width:1200px;height:560px;background:var(--navy)}
.ins-title{left:124px;top:1925px;font-size:28px;line-height:34px;color:var(--white)}
.ins-text{left:124px;top:2009px;width:360px;font-size:11.5px;line-height:18px;color:#e6ebf0}
.post{position:absolute;left:550px;width:526px;height:198px;background:var(--navy-card)}
.post .art{left:9px;top:9px;width:206px;height:180px}
.post-date{position:absolute;left:242px;top:27px;font-size:11px;color:#e6ebf0;display:flex;gap:9px;align-items:center}
.post h3{position:absolute;left:242px;top:52px;font-size:18.5px;font-weight:500;color:var(--white)}
.post p{position:absolute;left:242px;top:88px;width:270px;font-size:11.5px;line-height:18px;color:#e6ebf0}
.post .btn{left:242px;top:138px;width:110px;height:30px}

/* contact */
.con-title{left:153px;top:2503px;font-size:28px;line-height:34px}
.con-text{left:153px;top:2592px;width:380px;font-size:11.5px;line-height:18px;color:var(--muted)}
.con-item{position:absolute;left:153px;display:flex;gap:19px}
.con-icon{width:39px;height:39px;background:var(--navy);display:flex;align-items:center;justify-content:center}
.con-item b{display:block;font-weight:400;font-size:16px;line-height:20px}
.con-item span{font-size:11.5px;color:var(--muted)}
.field{position:absolute;background:var(--field);font-size:14px;color:var(--ink);padding:21px 0 0 29px;line-height:1}

/* footer */
.foot-bg{left:0;top:2891px;width:1200px;height:227px;background:var(--soft)}
.foot-text{left:125px;top:3040px;width:290px;font-size:11.5px;line-height:18px;color:var(--muted)}
.foot-col{position:absolute;top:2950px}
.foot-col h4{font-family:"Michroma",sans-serif;font-weight:400;font-size:13px;text-transform:uppercase;color:var(--navy);margin-bottom:11px}
.foot-col a{display:block;font-size:11.5px;line-height:20px;color:var(--muted);text-decoration:none}
.foot-rule{left:125px;top:3194px;width:951px;height:1px;background:#c9ced4}
.copy{left:125px;top:3207px;font-size:10px;color:var(--muted)}
.social{position:absolute;top:3207px;width:15px;height:15px;background:var(--coral);border-radius:3px}
</style>
</head>
<body>

<!-- header -->
<header>
  <div class="abs brand" style="left:144px;top:20px;font-size:15px"><span class="brand-dot" style="width:36px;height:36px"></span>Veranto</div>
  <nav class="nav">
    <a style="left:0">Home</a><a style="left:59px">About Us</a><a style="left:134px">Services</a><a style="left:206px">Insights</a><a style="left:275px">Contact</a>
  </nav>
  <div class="btn" style="left:919px;top:21px;width:152px;height:33px">Become A Sponsor</div>
</header>

<!-- hero -->
<section class="hero">
  <div class="art" role="img" aria-label="Soft grey botanical flower sprigs with coral blossoms" style="left:0;top:80px;width:140px;height:600px;background:linear-gradient(180deg,#fbeceb 0%,#f1f1f1 50%,#fafafa 100%);opacity:.7"></div>
  <div class="art" role="img" aria-label="Grey brush stroke texture" style="left:620px;top:150px;width:520px;height:530px;background:radial-gradient(ellipse at 60% 60%,#e3e6ea 0%,#f2f3f5 55%,transparent 75%)"></div>
  <h1 class="abs display hero-title">Connecting<br>Japanese and<br>European Art</h1>
  <p class="abs hero-sub">Empowering Emerging Artists, Curating Cross-Cultural Exhibitions, And Bridging Global Creative Communities.</p>
  <div class="btn" style="left:123px;top:437px;width:157px;height:31px">Explore Our Mission</div>
  <div class="abs" style="left:618px;top:150px;width:355px;height:414px;border-right:2px solid #8a9099;border-bottom:2px solid #8a9099"></div>
  <div class="art" role="img" aria-label="Collage artwork of a portrait with flowers in coral, navy and beige" style="left:610px;top:142px;width:355px;height:414px;background:linear-gradient(160deg,#e6dccb 0%,#cfc2ad 35%,#3a3d44 60%,#24344d 100%)"></div>
  <div class="abs view-box">View<br>Exhibition
    <span class="corner-arrow" style="left:91px;top:82px"><svg width="9" height="9" viewBox="0 0 9 9"><path d="M1 8 8 1M3 1h5v5" stroke="#fff" stroke-width="1.2" fill="none"/></svg></span>
  </div>
</section>

<!-- who we are -->
<section>
  <div class="abs who-bg"></div>
  <svg class="abs" style="left:905px;top:968px" width="300" height="320" viewBox="0 0 300 320"><circle cx="162" cy="160" r="155" fill="none" stroke="#ebebeb" stroke-width="6"/></svg>
  <div class="abs who-card">
    <div class="art" role="img" aria-label="Abstract collage face artwork in black, red, yellow and teal" style="left:15px;top:19px;width:272px;height:254px;background:linear-gradient(135deg,#efe8d9 0%,#d9b36c 30%,#c9443d 55%,#1c1c1c 80%,#efe8d9 100%)"></div>
    <div class="abs" style="left:0;top:290px;width:302px;text-align:center;font-size:36px;letter-spacing:6px;color:var(--navy);text-transform:uppercase">Veranto</div>
  </div>
  <h2 class="abs display who-title">Who We Are</h2>
  <p class="abs who-text">We Are An Institution Dedicated To The Communication And Promotion Of Contemporary Art And Design Across Japan And Europe. Our Mission Is To Create Meaningful Cultural Connections By Organizing Exhibitions, Fostering Artistic Exchange, And Enabling Sponsors To Support Impactful Creative Projects.<br>We Aim To Build Spaces Where Artists, Audiences, And Institutions Can Meet, Interact, And Grow Beyond Their Cultural Boundaries.</p>
  <ul class="abs checks">
    <li><svg width="14" height="14" viewBox="0 0 14 14"><circle cx="7" cy="7" r="6" fill="none" stroke="#142c46" stroke-width="1.3"/><path d="M4 7.2 6.2 9.3 10.3 4.8" fill="none" stroke="#142c46" stroke-width="1.3"/></svg>Cultural Exchange</li>
    <li><svg width="14" height="14" viewBox="0 0 14 14"><circle cx="7" cy="7" r="6" fill="none" stroke="#142c46" stroke-width="1.3"/><path d="M4 7.2 6.2 9.3 10.3 4.8" fill="none" stroke="#142c46" stroke-width="1.3"/></svg>Artist Empowerment</li>
    <li><svg width="14" height="14" viewBox="0 0 14 14"><circle cx="7" cy="7" r="6" fill="none" stroke="#142c46" stroke-width="1.3"/><path d="M4 7.2 6.2 9.3 10.3 4.8" fill="none" stroke="#142c46" stroke-width="1.3"/></svg>Cross-Regional Collaboration</li>
  </ul>
  <div class="btn" style="left:481px;top:1078px;width:147px;height:32px">Resquest A Quote</div>
</section>

<!-- services -->
<section>
  <h2 class="abs display svc-title">Curating Connections<br>Through Our Services</h2>
  <div class="svc-card" style="left:124px">
    <div class="art" role="img" aria-label="Gallery room with posters on white walls and display tables" style="inset:0;background:linear-gradient(180deg,#ecebea 0%,#d6d3d0 55%,#b9b6b3 100%)"></div>
    <span class="corner-arrow" style="left:270px;top:14px"><svg width="9" height="9" viewBox="0 0 9 9"><path d="M1 8 8 1M3 1h5v5" stroke="#fff" stroke-width="1.2" fill="none"/></svg></span>
    <div class="svc-label">Exhibition Organisation</div>
  </div>
  <div class="svc-card" style="left:448px">
    <div class="art" role="img" aria-label="Grey exhibition space with framed works and a glass vitrine" style="inset:0;background:linear-gradient(180deg,#6f6f72 0%,#8d8c8b 50%,#a9a7a4 100%)"></div>
    <span class="corner-arrow" style="left:270px;top:14px"><svg width="9" height="9" viewBox="0 0 9 9"><path d="M1 8 8 1M3 1h5v5" stroke="#fff" stroke-width="1.2" fill="none"/></svg></span>
    <div class="svc-label dark">Sponsorship Programs</div>
  </div>
  <div class="svc-card" style="left:771px">
    <div class="art" role="img" aria-label="Two artists painting together at an easel" style="inset:0;background:linear-gradient(135deg,#e3703e 0%,#c98a3a 40%,#6b5a3a 75%,#3a2a20 100%)"></div>
    <span class="corner-arrow" style="left:270px;top:14px"><svg width="9" height="9" viewBox="0 0 9 9"><path d="M1 8 8 1M3 1h5v5" stroke="#fff" stroke-width="1.2" fill="none"/></svg></span>
    <div class="svc-label">Artist Support</div>
  </div>
</section>

<!-- insights -->
<section>
  <div class="abs ins-bg"></div>
  <div class="art" role="img" aria-label="Dark blue brush stroke texture" style="left:0;top:2080px;width:520px;height:337px;background:radial-gradient(ellipse at 40% 50%,#23405f 0%,transparent 70%)"></div>
  <h2 class="abs display ins-title">Latest<br>Insights</h2>
  <p class="abs ins-text">Lorem Ipsum Dolor Sit Amet Consectetur. Sagittis Sit Facilisis Libero Eget Dolor Enim Non Maecenas.</p>
  <div class="btn" style="left:124px;top:2064px;width:148px;height:32px">Resquest A Quote</div>

  <article class="post" style="top:1934px">
    <div class="art" role="img" aria-label="Visitors discussing artworks in a gallery" style="background:linear-gradient(135deg,#d9d6d0 0%,#9c8f80 50%,#4b4a48 100%)"></div>
    <div class="post-date"><svg width="11" height="11" viewBox="0 0 11 11"><rect x="1" y="2" width="9" height="8" fill="none" stroke="#fff"/><path d="M1 4.5h9M3.5 1v2M7.5 1v2" stroke="#fff"/></svg>17-11-25</div>
    <h3>Lorem Ipsum Dolor Sit Amet</h3>
    <p>Lorem Ipsum Dolor Sit Amet Consectetur. Eget Dolor Enim Non Maecenas.</p>
    <div class="btn">Learn More</div>
  </article>
  <article class="post" style="top:2151px">
    <div class="art" role="img" aria-label="Two people holding a framed blue painting" style="background:linear-gradient(135deg,#1e4e5e 0%,#c9a24a 35%,#e9e6e0 60%,#7d8a5a 100%)"></div>
    <div class="post-date"><svg width="11" height="11" viewBox="0 0 11 11"><rect x="1" y="2" width="9" height="8" fill="none" stroke="#fff"/><path d="M1 4.5h9M3.5 1v2M7.5 1v2" stroke="#fff"/></svg>17-11-25</div>
    <h3>Lorem Ipsum Dolor Sit Amet</h3>
    <p>Lorem Ipsum Dolor Sit Amet Consectetur. Eget Dolor Enim Non Maecenas.</p>
    <div class="btn">Learn More</div>
  </article>
</section>

<!-- contact -->
<section>
  <h2 class="abs display con-title">Connect<br>With Us</h2>
  <p class="abs con-text">Lorem Ipsum Dolor Sit Amet Consectetur. Nunc Pulvinar In Quam Faucibus. Adipiscing Mollis Dolor.</p>
  <div class="con-item" style="top:2654px">
    <div class="con-icon"><svg width="13" height="13" viewBox="0 0 13 13"><path d="M3 1 5 4 3.8 5.3C4.6 7 6 8.4 7.7 9.2L9 8l3 2-1 2C6 12 1 7 1 2z" fill="#fff"/></svg></div>
    <div><b>Phone</b><span>+(000)-000-0000</span></div>
  </div>
  <div class="con-item" style="top:2705px">
    <div class="con-icon"><svg width="13" height="10" viewBox="0 0 13 10"><rect width="13" height="10" fill="#fff"/><path d="M0 0 6.5 5.5 13 0" fill="none" stroke="#142c46" stroke-width="1.2"/></svg></div>
    <div><b>Email</b><span>Info@Veranto.Com</span></div>
  </div>
  <div class="con-item" style="top:2756px">
    <div class="con-icon"><svg width="11" height="14" viewBox="0 0 11 14"><path d="M5.5 0A5.5 5.5 0 0 0 0 5.5C0 9 5.5 14 5.5 14S11 9 11 5.5A5.5 5.5 0 0 0 5.5 0z" fill="#fff"/><circle cx="5.5" cy="5.5" r="2" fill="#142c46"/></svg></div>
    <div><b>Address</b><span>Lorem Ipsum Dolor Sit Amet Consectetur.</span></div>
  </div>
  <form>
    <div class="field" style="left:575px;top:2511px;width:229px;height:43px">Name</div>
    <div class="field" style="left:817px;top:2511px;width:230px;height:43px">Email</div>
    <div class="field" style="left:575px;top:2568px;width:229px;height:43px">Phone</div>
    <div class="field" style="left:817px;top:2568px;width:230px;height:43px">Services
      <svg class="abs" style="right:18px;top:19px" width="8" height="5" viewBox="0 0 8 5"><path d="M0 0h8L4 5z" fill="#142c46"/></svg></div>
    <div class="field" style="left:575px;top:2625px;width:472px;height:120px">Message</div>
    <div class="btn" style="left:575px;top:2758px;width:472px;height:38px;font-size:14px">Contact Us</div>
  </form>
</section>

<!-- footer -->
<footer>
  <div class="abs foot-bg"></div>
  <div class="abs brand" style="left:125px;top:2954px;font-size:22px;gap:22px"><span class="brand-dot" style="width:58px;height:58px"></span>Veranto</div>
  <p class="abs foot-text">We Are An Institution Dedicated To The Communication And Promotion Of Contemporary Art And Design Across Japan And Europe.</p>
  <div class="foot-col" style="left:641px"><h4>Company</h4><a>Home</a><a>About Us</a><a>Services</a><a>Insights</a><a>Contact</a></div>
  <div class="foot-col" style="left:799px"><h4>Resources</h4><a>Lorem Ipsum Dolor</a><a>Lorem Ipsum Dolor</a><a>Lorem Ipsum Dolor</a><a>Lorem Ipsum Dolor</a></div>
  <div class="foot-col" style="left:980px"><h4>Legal</h4><a>Terms Of Service</a><a>Privacy Policy</a><a>Cookies Policy</a></div>
  <div class="abs foot-rule"></div>
  <p class="abs copy">© Copyright 2025, All Rights Reserved By Veranto</p>
  <span class="social" style="left:1029px"></span>
  <span class="social" style="left:1059px"></span>
</footer>

</body>
</html>
```